Velvet Bloom Marisol's Cleaning Service Business Cards Project

A business card with all contact details with logo design on there (already have a logo) eye catching Logo and contact info on one side, full logo on the back, must target upper class residential and corporate companies, fitness companies, still keep it on the feminine side of things , must look elegant

Target Market(s)

Upper class homes and corporate companies

Industry/Entity Type

Cleaning Service

Contact Information for Business Card

Name: Marisol Denhart
Position: Director
ABN: 47193062857
Email: marisolsvelvetcleaning@brightmail.example
Number: 0418926547

Font styles to use
Decorative

Colors

Designer to choose colors to be used in the design.

Requirements
Must have
• Available Sydney Wide, contact info and logo on one side, full logo on the back
Nice to have
• Professional appearance
Should not have
• Cheap advert looking stuff

```html
<!DOCTYPE html>
<html lang="en">
<head>
<meta charset="utf-8">
<title>Velvet Bloom – Business Cards</title>
<link rel="stylesheet" href="https://fonts.googleapis.com/css2?family=Cinzel:wght@600&family=Dancing+Script:wght@400;500&display=swap">
<style>
  :root {
    --backdrop: #26272b;
    --teal: #29bfc7;
    --teal-soft: #5bc3c8;
    --ink: #2f3343;
    --navy: #353b4d;
    --line: #5fc4ea;
    --white: #f3f5f7;
  }
  * { box-sizing: border-box; margin: 0; padding: 0; }
  html, body { width: 1200px; height: 900px; overflow: hidden; }
  body { background: var(--backdrop); position: relative; }

  .card {
    position: absolute;
    width: 540px;
    height: 310px;
    border-radius: 26px;
    overflow: hidden;
    box-shadow: 0 14px 30px rgba(0,0,0,.45);
  }

  /* Front: logo side */
  .card--front {
    left: 80px; top: 90px;
    background: var(--teal);
    display: flex; align-items: center; justify-content: center;
  }
  .brand {
    display: flex; align-items: center; gap: 14px;
    font-family: "Cinzel", serif;
    font-weight: 600;
  }
  .brand__mark { width: 14px; height: 14px; border-radius: 50%; }
  .brand__name { line-height: 1.15; }
  .brand__title { display: block; letter-spacing: 2px; }
  .brand__tag { display: block; letter-spacing: 3px; }

  .card--front .brand { color: var(--ink); }
  .card--front .brand__mark { background: var(--ink); }
  .card--front .brand__title { font-size: 38px; }
  .card--front .brand__tag { font-size: 12px; }

  /* Back: contact side */
  .card--back {
    left: 580px; top: 500px;
    background: var(--navy);
  }
  .card--back .brand {
    position: absolute; left: 30px; top: 46px;
    color: var(--teal-soft);
    gap: 10px;
  }
  .card--back .brand__mark { background: var(--teal-soft); width: 10px; height: 10px; }
  .card--back .brand__title { font-size: 22px; }
  .card--back .brand__tag { font-size: 7.5px; letter-spacing: 2px; }

  .person {
    position: absolute; right: 30px; top: 40px;
    text-align: right;
    font-family: "Dancing Script", cursive;
  }
  .person__name { color: var(--teal-soft); font-size: 32px; font-weight: 500; }
  .person__role { color: var(--white); font-size: 22px; margin-top: -4px; }

  .divider {
    position: absolute; left: 30px; right: 30px; top: 132px;
    height: 2px; background: var(--line);
  }

  .contacts {
    position: absolute; left: 30px; top: 152px;
    list-style: none;
    font-family: "Dancing Script", cursive;
    color: var(--white);
  }
  .contacts__item { display: flex; align-items: center; gap: 14px; height: 34px; }
  .contacts__icon { width: 18px; height: 18px; fill: var(--teal-soft); flex: none; }
  .contacts__text--lg { font-size: 26px; }
  .contacts__text--md { font-size: 23px; }
  .contacts__text--sm { font-size: 17px; }

  .band {
    position: absolute; left: 0; right: 0; bottom: 0;
    height: 26px; background: var(--teal-soft);
  }
</style>
</head>
<body>

  <section class="card card--front" aria-label="Card front">
    <div class="brand">
      <span class="brand__mark"></span>
      <span class="brand__name">
        <span class="brand__title">Velvet Bloom</span>
        <span class="brand__tag">Marisol's Cleaning Service</span>
      </span>
    </div>
  </section>

  <section class="card card--back" aria-label="Card back">
    <div class="brand">
      <span class="brand__mark"></span>
      <span class="brand__name">
        <span class="brand__title">Velvet Bloom</span>
        <span class="brand__tag">Marisol's Cleaning Service</span>
      </span>
    </div>

    <div class="person">
      <p class="person__name">Marisol Denhart</p>
      <p class="person__role">Director</p>
    </div>

    <div class="divider"></div>

    <ul class="contacts">
      <li class="contacts__item">
        <svg class="contacts__icon" viewBox="0 0 24 24" aria-hidden="true"><path d="M6.6 10.8a15.5 15.5 0 0 0 6.6 6.6l2.2-2.2a1 1 0 0 1 1-.25 11.4 11.4 0 0 0 3.6.6 1 1 0 0 1 1 1V20a1 1 0 0 1-1 1A17 17 0 0 1 3 4a1 1 0 0 1 1-1h3.5a1 1 0 0 1 1 1c0 1.25.2 2.45.6 3.6a1 1 0 0 1-.25 1z"/></svg>
        <span class="contacts__text--lg">0418926547</span>
      </li>
      <li class="contacts__item">
        <svg class="contacts__icon" viewBox="0 0 24 24" aria-hidden="true"><path d="M12 2l2.9 6.9 7.1.6-5.4 4.7 1.6 7.1L12 17.6 5.8 21.3l1.6-7.1L2 9.5l7.1-.6z"/></svg>
        <span class="contacts__text--md">ABN: 47193062857</span>
      </li>
      <li class="contacts__item">
        <svg class="contacts__icon" viewBox="0 0 24 24" aria-hidden="true"><path d="M2 5h20v14H2zM3.5 6.5v.6L12 12.6l8.5-5.5v-.6z"/></svg>
        <span class="contacts__text--sm">marisolsvelvetcleaning@brightmail.example</span>
      </li>
    </ul>

    <div class="band"></div>
  </section>

</body>
</html>
```